Company Brochure promoting our Managed Services Business (MSP)

Objective: Is the brochure meant to generate leads, educate potential clients, and promote our Managed Services Business.
Target Audience: is for Small to medium size business.
A managed service provider like Brillora Advisory Group handles a variety of different responsibilities for Business
. We oversee vital IT resources such as:
Email
Cloud integration
Data storage
Networking
Cybersecurity
File backup
Help desk services
Our firm also provides remote monitoring services and updates. As part of our managed service provider solutions, we will continually report on the performance and quality of your network. We can even help your organization acquire new hardware and software.
At Brillora Advisory Group we specialize in empowering commercial businesses with robust IT solutions tailored to enhance efficiency, security, and scalability. With years of expertise in Managed Services, we understand the unique challenges businesses face in today’s digital landscape.
Call-to-Action (CTA):
Encourage readers to contact you, visit your website, or schedule a consultation.
you can get an overview of BAG at www..brillorabag.example.
Layout: Opt for a clean, easy-to-read layout with well-defined sections.
Imagery:
Include professional photos, custom graphics, or icons that represent your services.
Avoid generic stock images when possible.
Format: Tri-fold, bi-fold, depending on the amount of information.
We would like to have a section of the "e5" from our web site.
I have attached the Logos.
Target Market(s)
Small to Medium Business
Look and feel

```html
<!DOCTYPE html>
<html lang="en">
<head>
<meta charset="utf-8">
<title>Brillora Advisory Group – Tri-fold Brochure</title>
<link href="https://fonts.googleapis.com/css2?family=Inter:wght@400;500;600;700;800&display=swap" rel="stylesheet">
<style>
:root{
  --teal-deep:#12495a;
  --teal:#1a5a6d;
  --teal-band:#3a8397;
  --ink:#1f2a30;
  --paper:#ffffff;
  --soft-text:#e6f0f3;
}
*{box-sizing:border-box;margin:0;padding:0}
html,body{width:1200px;height:3229px;overflow:hidden}
body{background:linear-gradient(180deg,#f1f1f1,#e4e5e6);font-family:"Inter",Arial,sans-serif;color:var(--ink);position:relative}
.spread{position:absolute;left:50px;width:1100px;height:854px;background:var(--paper);box-shadow:0 10px 30px rgba(0,0,0,.18);overflow:hidden}
.spread--outside{top:680px}
.spread--inside{top:1694px}
.block{position:absolute}
.photo{position:absolute}
.dark{background:var(--teal-deep);color:#fff}

/* brand lockup: plain square + name in one weight */
.brand{display:flex;align-items:center;gap:12px}
.brand-square{width:22px;height:22px;flex:0 0 22px}
.brand-name{font-size:18px;font-weight:600;line-height:1.2}

/* outside: why choose */
.why{left:0;top:0;width:367px;height:470px;padding:44px 34px}
.why h2{font-size:22px;font-weight:700;line-height:1.2}
.rule{width:84px;height:3px;background:var(--teal);margin:18px 0 26px}
.feature{display:flex;gap:16px;margin-bottom:28px}
.feature svg{flex:0 0 34px;height:34px}
.feature h3{font-size:14px;font-weight:700;margin-bottom:2px}
.feature p{font-size:13px;line-height:1.38}
.why-photo{left:0;top:470px;width:367px;height:384px;background:linear-gradient(160deg,#dfe6ec 0%,#a9bccb 45%,#4e7ea6 75%,#2d5a7f 100%)}

/* outside: contact */
.contact{left:367px;top:0;width:366px;height:470px;text-align:center;padding:40px 30px}
.contact h2{font-size:21px;font-weight:700;line-height:1.22;text-transform:uppercase;margin-bottom:34px}
.contact .label{font-size:10px;font-weight:700;text-transform:uppercase;letter-spacing:.04em;margin-bottom:5px}
.contact .value{font-size:13px;line-height:1.45;margin-bottom:20px;color:var(--soft-text)}
.logo-band{left:367px;top:470px;width:366px;height:151px;display:flex;align-items:center;justify-content:center}
.logo-band .brand-square{background:var(--teal-deep)}
.logo-band .brand-name{color:var(--teal-deep)}
.partners{left:367px;top:621px;width:366px;height:233px;padding:16px 30px}
.partners h3{font-size:19px;font-weight:600;text-align:center;margin-bottom:16px}
.partner-grid{display:grid;grid-template-columns:repeat(3,1fr);gap:12px 16px}
.partner{height:38px;background:#fff;display:flex;align-items:center;justify-content:center}
.partner span{width:60%;height:14px;background:#9fb3bc;border-radius:3px}

/* outside: cover */
.cover-photo{left:733px;top:0;width:367px;height:470px;background:radial-gradient(circle at 55% 45%,#f2d7b0 0%,#5aa6d6 18%,#1f5d8f 45%,#0d2a45 80%)}
.cover-mark{left:765px;top:30px}
.cover-mark .brand-square{background:#fff}
.cover-mark .brand-name{color:#fff}
.cover-headline{left:733px;top:470px;width:367px;height:151px;padding:22px 12px 0 30px}
.cover-headline h1{font-size:31px;font-weight:700;line-height:1.12;color:var(--teal)}
.cover-tag{left:733px;top:621px;width:367px;height:233px;padding:26px 30px;font-size:15px;line-height:1.45;color:var(--soft-text)}

/* inside */
.about{left:0;top:0;width:733px;height:274px}
.about-col{position:absolute;top:0;width:366px;height:274px;padding:30px 34px;color:#fff}
.about-col + .about-col{border-left:1px solid rgba(255,255,255,.15)}
.about h2{font-size:32px;font-weight:700;margin-bottom:20px}
.about h3{font-size:13px;font-weight:700;margin-bottom:6px}
.about p{font-size:12.5px;line-height:1.45;color:var(--soft-text)}
.services-photo{left:0;top:274px;width:733px;height:476px;background:linear-gradient(135deg,#0f3346 0%,#1e5a78 40%,#3f86a8 60%,#0e2d40 100%)}
.services-panel{left:0;top:370px;width:706px;height:320px;background:rgba(230,238,242,.86);border-radius:0 14px 14px 0}
.services-title{left:34px;top:382px;font-size:32px;font-weight:700;line-height:1.05;color:var(--ink)}
.service{position:absolute;display:flex;gap:12px;width:310px}
.service svg{flex:0 0 30px;height:30px}
.service h4{font-size:13px;font-weight:700;margin-bottom:2px}
.service p{font-size:12px;line-height:1.38}
.foot{top:750px;height:104px;background:var(--teal-band);color:#fff;display:flex;align-items:center;justify-content:center;text-align:center}
.foot--phone{left:0;width:366px;font-size:19px;font-weight:500}
.foot--web{left:366px;width:367px;font-size:15px;font-weight:600}
.foot--method{left:733px;width:367px;font-size:12.5px;line-height:1.35;padding:0 34px}

.method{left:733px;top:0;width:367px;height:750px;padding:34px 30px}
.method h2{font-size:21px;font-weight:700;line-height:1.2;margin-bottom:20px}
.step{display:flex;gap:14px;margin-bottom:20px}
.step svg{flex:0 0 30px;height:30px}
.step h4{font-size:13px;font-weight:700;margin-bottom:2px}
.step p{font-size:12px;line-height:1.38}
.method-badge{position:absolute;left:848px;top:565px;width:140px;height:140px}
</style>
</head>
<body>

<section class="spread spread--outside" aria-label="Brochure outside">
  <div class="block why">
    <h2>Why Choose Brillora<br>Advisory Group?</h2>
    <div class="rule"></div>
    <div class="feature">
      <svg viewBox="0 0 34 34" fill="none" stroke="#1f2a30" stroke-width="1.6"><circle cx="17" cy="14" r="8"/><path d="M12 21l-3 10 8-4 8 4-3-10"/></svg>
      <div><h3>150+ Years of Expertise:</h3><p>A wealth of experience delivering innovative IT solutions.</p></div>
    </div>
    <div class="feature">
      <svg viewBox="0 0 34 34" fill="none" stroke="#1f2a30" stroke-width="1.6"><rect x="4" y="4" width="12" height="12"/><rect x="18" y="18" width="12" height="12"/><path d="M16 10h6v8M10 16v8h8"/></svg>
      <div><h3>Tailored Strategies:</h3><p>Personalized solutions designed to meet your unique business goals.</p></div>
    </div>
    <div class="feature">
      <svg viewBox="0 0 34 34" fill="none" stroke="#1f2a30" stroke-width="1.6"><rect x="5" y="4" width="20" height="26" rx="2"/><path d="M9 11h12M9 16h12M9 21h8"/><circle cx="26" cy="25" r="5"/></svg>
      <div><h3>Long-Term Partnerships:</h3><p>We're committed to your growth and success.</p></div>
    </div>
  </div>
  <div class="photo why-photo" role="img" aria-label="Photo of a team reviewing printed business charts on a desk"></div>

  <div class="block contact dark">
    <h2>Get Started with<br>Brillora MSP<br>Services Today</h2>
    <div class="label">HQ Address</div>
    <div class="value">820 Harbor Crest Lane<br>Suite 210<br>Coral Bend, FL 32000</div>
    <div class="label">Locations</div>
    <div class="value">Palm Reach - Lakeview - Cedar Point<br>Sandy Bay - Ashford</div>
    <div class="label">Phone</div>
    <div class="value">1-855-BRILLOR</div>
    <div class="label">Email</div>
    <div class="value">sales@brillorabag.example</div>
  </div>
  <div class="block logo-band">
    <div class="brand"><span class="brand-square"></span><span class="brand-name">Brillora Advisory Group</span></div>
  </div>
  <div class="block partners dark">
    <h3>Our Partners</h3>
    <div class="partner-grid">
      <div class="partner"><span></span></div><div class="partner"><span></span></div><div class="partner"><span></span></div>
      <div class="partner"><span></span></div><div class="partner"><span></span></div><div class="partner"><span></span></div>
      <div class="partner"><span></span></div><div class="partner"><span></span></div><div class="partner"><span></span></div>
    </div>
  </div>

  <div class="photo cover-photo" role="img" aria-label="Illustration of a hand touching a glowing digital interface"></div>
  <div class="block cover-mark"><div class="brand"><span class="brand-square"></span><span class="brand-name">Brillora Advisory Group</span></div></div>
  <div class="block cover-headline"><h1>Empowering Businesses in the Digital Age</h1></div>
  <div class="block cover-tag dark">Your trusted partner in delivering innovative IT solutions, enhancing efficiency, and driving success.</div>
</section>

<section class="spread spread--inside" aria-label="Brochure inside">
  <div class="block about dark">
    <div class="about-col" style="left:0">
      <h2>About Us</h2>
      <h3>Empowering Your Digital Future</h3>
      <p>At Brillora Advisory Group, we transform businesses with cutting-edge technology solutions. Our expert consultants streamline operations, enhance security, and drive innovation, ensuring you stay ahead of the competition.</p>
    </div>
    <div class="about-col" style="left:366px;padding-top:90px">
      <h3>Empowering Your Digital Future</h3>
      <p>Our VisionTo empower businesses of all sizes with tailored IT solutions, fostering growth and success in an ever-evolving digital landscape.</p>
    </div>
  </div>
  <div class="photo services-photo" role="img" aria-label="Photo of a blue-lit server room with digital overlay graphics"></div>
  <div class="block services-panel"></div>
  <div class="block services-title">Our<br>Services</div>

  <div class="service" style="left:34px;top:500px">
    <svg viewBox="0 0 30 30" fill="none" stroke="#1f2a30" stroke-width="1.6"><circle cx="15" cy="15" r="6"/><circle cx="15" cy="15" r="11" stroke-dasharray="4 3"/></svg>
    <div><h4>Managed Services</h4><p>Leave your IT to the experts! We monitor and manage your networks, security, and software to keep your business running smoothly.</p></div>
  </div>
  <div class="service" style="left:34px;top:600px">
    <svg viewBox="0 0 30 30" fill="none" stroke="#1f2a30" stroke-width="1.6"><rect x="5" y="3" width="18" height="24" rx="2"/><path d="M9 9h10M9 14h10M9 19h6"/></svg>
    <div><h4>Account Management</h4><p>Focus on growth while we handle RFPs, contracts, and service renewals with precision and expertise.</p></div>
  </div>
  <div class="service" style="left:390px;top:400px">
    <svg viewBox="0 0 30 30" fill="none" stroke="#1f2a30" stroke-width="1.6"><circle cx="15" cy="15" r="5"/><path d="M15 3v5M15 22v5M3 15h5M22 15h5M7 7l3 3M20 20l3 3M23 7l-3 3M7 23l3-3"/></svg>
    <div><h4>Business Technologies</h4><p>Work smarter, not harder! We integrate advanced tools for efficiency, communication, security, and future-proofing.</p></div>
  </div>
  <div class="service" style="left:390px;top:503px">
    <svg viewBox="0 0 30 30" fill="none" stroke="#1f2a30" stroke-width="1.6"><rect x="3" y="5" width="24" height="16" rx="1"/><path d="M10 26h10M15 21v5M8 11h8M8 15h12"/></svg>
    <div><h4>Training &amp; Education</h4><p>Empower your team with tailored programs designed to enhance skills and boost performance.</p></div>
  </div>
  <div class="service" style="left:390px;top:586px">
    <svg viewBox="0 0 30 30" fill="none" stroke="#1f2a30" stroke-width="1.6"><circle cx="10" cy="10" r="5"/><circle cx="20" cy="20" r="5"/><path d="M14 14l2 2"/></svg>
    <div><h4>Workflow Management</h4><p>Streamline your processes with intuitive tools for documentation, monitoring, and continuous improvement.</p></div>
  </div>

  <div class="block method">
    <h2>Our Methodology:<br>The Five-Step Growth Cycle</h2>
    <div class="step"><svg viewBox="0 0 30 30" fill="none" stroke="#1f2a30" stroke-width="1.6"><circle cx="13" cy="13" r="8"/><path d="M19 19l7 7"/></svg><div><h4>Evaluate</h4><p>Analyze your current systems and gather insights to identify challenges and opportunities.</p></div></div>
    <div class="step"><svg viewBox="0 0 30 30" fill="none" stroke="#1f2a30" stroke-width="1.6"><circle cx="15" cy="15" r="10"/><path d="M10 17l4-4 3 3 4-5"/></svg><div><h4>Enhance</h4><p>Optimize workflows, streamline inefficiencies, and implement best practices.</p></div></div>
    <div class="step"><svg viewBox="0 0 30 30" fill="none" stroke="#1f2a30" stroke-width="1.6"><rect x="4" y="6" width="22" height="18"/><path d="M8 20l5-6 4 4 5-7"/></svg><div><h4>Engineer</h4><p>Design and structure tailored solutions aligned with your goals.</p></div></div>
    <div class="step"><svg viewBox="0 0 30 30" fill="none" stroke="#1f2a30" stroke-width="1.6"><rect x="6" y="4" width="18" height="23" rx="2"/><path d="M10 12l3 3 6-6M10 21h10"/></svg><div><h4>Execute</h4><p>Implement strategies with precision and transparency, ensuring milestones are met.</p></div></div>
    <div class="step"><svg viewBox="0 0 30 30" fill="none" stroke="#1f2a30" stroke-width="1.6"><path d="M25 15a10 10 0 1 1-3-7"/><path d="M23 4v5h-5"/></svg><div><h4>Evolve</h4><p>Adapt and innovate through continuous improvement and regular reviews.</p></div></div>
  </div>
  <svg class="method-badge" viewBox="0 0 140 140" aria-hidden="true">
    <circle cx="70" cy="70" r="66" fill="none" stroke="#1f2a30" stroke-width="3"/>
    <circle cx="70" cy="70" r="44" fill="#12495a"/>
  </svg>

  <div class="block foot foot--phone">1-855-BRILLOR</div>
  <div class="block foot foot--web">www.brillorabag.example</div>
  <div class="block foot foot--method">Let Brillora's proven methodology position your business for long-term success!</div>
</section>

</body>
</html>
```